Serial Entrepreneur Business Card: 4 Logo Design

I am a serial entrepreneur and a full time mechanical engineer. I have four businesses. I would like to display them all on one business card.
*Please see the attached PDF for the design requirements*

www.KelbroNest.com

Businesses
-KelbroNest
-Quiet Lantern Properties
-Torlen Products
-Drosk Harbor Cast

Target Market(s)

Clients, Entrepreneurs, Associates, really anyone. Should be very professional.

Industry/Entity Type

Entrepreneur

Contact Information for Business Card

3.5" x 2" Standard Business Card Size
** Please review the attached requirement PDF for in depth detail on what I am expecting**

Font styles to use
Sans Serif

Requirements
Must have
• My personal contact information:
• First Name: Dae hwan
• Last Name: Pellow
• Nick Name: Riko
• Address: 83 Tolmer Court, Garfield NJ 07392
• Phone Number: 201-574-2916
• Email: RikodPellow@mailnest.example
• Website: www.KelbroNest.com
• All Four Logos of the Companies I own:
• -KelbroNest
• -Quiet Lantern Properties
• -Torlen Products
• -Drosk Harbor Cast
• My Professions:
• -Prototyping Engineer
• -Real Estate Investor
• -Financial Blogger
• -Video Podcaster
• -Online Retail Seller
Nice to have
• If it fits, please include the website for each logo, if there is more space please include the email for each.
• It might be nice to have the QX GUILD Logo, or TOVRA logo for my full-time job. But only if it fits.

```html
<!DOCTYPE html>
<html lang="en">
<head>
<meta charset="utf-8">
<title>KelbroNest Business Card Back</title>
<link rel="stylesheet" href="https://fonts.googleapis.com/css2?family=Montserrat:wght@700;800&display=swap">
<style>
  :root {
    --paper: #f2f2f4;
    --ink: #0b0b0b;
    --green: #13894a;
    --red: #bd1e2d;
    --red-edge: #ee3a33;
  }
  html, body {
    margin: 0;
    padding: 0;
    width: 1200px;
    height: 1200px;
    overflow: hidden;
    background: var(--paper);
  }
  .canvas {
    position: relative;
    width: 1200px;
    height: 1200px;
    overflow: hidden;
    background: var(--paper);
  }
  .card {
    position: absolute;
    left: 0;
    top: 0;
    width: 1500px;
    height: 1500px;
    transform-origin: 0 0;
    transform: translate(0, 1200px) rotate(-90deg) scale(0.8);
    font-family: "Montserrat", "Helvetica Neue", Arial, sans-serif;
    color: var(--ink);
  }
  .brand-row {
    position: absolute;
    left: 0;
    width: 1500px;
    display: flex;
    justify-content: center;
    align-items: center;
    gap: 30px;
    white-space: nowrap;
  }
  .brand-mark {
    flex: none;
    display: block;
  }
  .brand-mark--green { background: var(--green); }
  .brand-mark--ink { background: var(--ink); }
  .brand-name {
    font-weight: 800;
    line-height: 1;
    letter-spacing: 1px;
  }
  .brand-name--green { color: var(--green); }
  .brand-name--ink { color: var(--ink); }
  .contact {
    position: absolute;
    left: 0;
    width: 1500px;
    text-align: center;
    white-space: nowrap;
    line-height: 1;
    font-weight: 800;
    font-size: 60px;
    letter-spacing: 1px;
  }
  .footer-site {
    position: absolute;
    top: 1326px;
    left: 0;
    width: 1500px;
    display: flex;
    justify-content: center;
    align-items: center;
    gap: 30px;
    font-weight: 800;
    font-size: 68px;
    letter-spacing: 2px;
    line-height: 1;
  }
  .globe { width: 64px; height: 64px; }
  .accent-band {
    position: absolute;
    left: 0;
    top: 0;
    width: 1500px;
    height: 1500px;
    pointer-events: none;
  }
</style>
</head>
<body>
<div class="canvas">
  <div class="card">
    <svg class="accent-band" viewBox="0 0 1500 1500" aria-hidden="true">
      <polygon points="-10,1510 45,1452 470,1452 525,1402 975,1402 1030,1452 1455,1452 1510,1510"
               fill="var(--red)"/>
      <polyline points="-10,1510 45,1452 470,1452 525,1402 975,1402 1030,1452 1455,1452 1510,1510"
                fill="none" stroke="var(--red-edge)" stroke-width="9"/>
    </svg>

    <section class="venture venture--kelbronest">
      <div class="brand-row" style="top:110px; height:170px;">
        <span class="brand-mark brand-mark--green" style="width:150px; height:150px;"></span>
        <span class="brand-name brand-name--green" style="font-size:96px;">KelbroNest</span>
      </div>
      <div class="contact" style="top:302px;">www.KelbroNest.com</div>
      <div class="contact" style="top:352px;">Riko@KelbroNest.com</div>
    </section>

    <section class="venture venture--torlen">
      <div class="brand-row" style="top:425px; height:160px;">
        <span class="brand-mark brand-mark--ink" style="width:140px; height:140px;"></span>
        <span class="brand-name brand-name--ink" style="font-size:86px;">Torlen Products</span>
      </div>
      <div class="contact" style="top:600px;">www.TorlenProducts.com</div>
      <div class="contact" style="top:650px;">Sales@TorlenProducts.com</div>
    </section>

    <section class="venture venture--drosk">
      <div class="brand-row" style="top:765px; height:130px;">
        <span class="brand-mark brand-mark--green" style="width:120px; height:120px;"></span>
        <span class="brand-name brand-name--green" style="font-size:82px;">Drosk Harbor Cast</span>
      </div>
      <div class="contact" style="top:908px;">www.DroskHarborCast.com</div>
      <div class="contact" style="top:958px;">Media@DroskHarborCast.com</div>
    </section>

    <section class="venture venture--quiet-lantern">
      <div class="brand-row" style="top:1045px; height:110px;">
        <span class="brand-mark brand-mark--ink" style="width:105px; height:105px;"></span>
        <span class="brand-name brand-name--ink" style="font-size:70px;">Quiet Lantern Properties</span>
      </div>
      <div class="contact" style="top:1164px;">www.QuietLanternProperties.com</div>
      <div class="contact" style="top:1214px;">Riko@QuietLanternProperties.com</div>
    </section>

    <div class="footer-site">
      <svg class="globe" viewBox="0 0 66 66" aria-hidden="true">
        <g fill="none" stroke="var(--ink)" stroke-width="4">
          <circle cx="33" cy="33" r="30"/>
          <ellipse cx="33" cy="33" rx="13" ry="30"/>
          <line x1="33" y1="3" x2="33" y2="63"/>
          <line x1="3" y1="33" x2="63" y2="33"/>
          <line x1="8" y1="18" x2="58" y2="18"/>
          <line x1="8" y1="48" x2="58" y2="48"/>
        </g>
      </svg>
      <span>www.KelbroNest.com</span>
    </div>
  </div>
</div>
</body>
</html>
```